International travel site frontpage redesign

We sell tours to Scandinavia through our website www.velmora-journeys.com. The website has become a bit old fashioned and we are in the process of making the website responsive. As you can see from the attached pictures the website will be wider with the responsive design, and our current design does not fit anymore.

Here is what we are looking for:
- A website that reflects a trustworthy and quality oriented company.
- Making the website more modern looking, but still recognisable (we want to keep the colours).
- keeping in mind that the age group of our customers are from 20-80 years old (most in their 60s).
- We want to remove the popular tours part and are instead looking to replace this with picture boxes the following subjects Scandinavia Specialist, Special Offers, Contact, Norway (or Norway Tours), Sweden (or Sweden Tours), Iceland (or Iceland Tours), Combination Tours. Possibly also Lapland, Winter, Northern Lights, Fjords and Capitals. Some of these categories can be smaller or perhaps half boxes; i.e. Winter and Northern lights in one. If we end up with four boxes per line perhaps we could add a social media box next to the three first ones.
- The above means that the left hand meny with Norway Tours, Sweden Tours etc will be redundant.
- we will add another line to the search Box (on the top): Destinations
- The top menu will have the same categories, but we need to add languages as the website will be in English and German.
- The footer must be changed
- We can take away the box to the right where it says "your window to booking the best of our world"

Reason: One of the decission makers had to go away on business last minute.

Target Market(s)

Travelling to Scandinavia is not low cost, so the website needs to appeal to those that can afford to travel to our destination.
The age group of our customers are from 20-80 years old (most in their 60s).

Industry/Entity Type

Travel

Number of Pages Required

1 page

Requirements
Should not have
• Flashy or cheap looking special offers...

```html
<!DOCTYPE html>
<html lang="en">
<head>
<meta charset="utf-8">
<title>Velmora Journeys – Tours to Scandinavia</title>
<link href="https://fonts.googleapis.com/css2?family=Cinzel:wght@500&family=Open+Sans:wght@300;400;600;700&display=swap" rel="stylesheet">
<style>
:root{
  --red:#a8141b;
  --red-dark:#8c0f15;
  --ink:#333;
  --muted:#777;
  --line:#e2e2e2;
  --panel:#efefef;
  --white:#fff;
  --footer:#2a2a2a;
  --footer-bottom:#1c1c1c;
  --footer-text:#bdbdbd;
}
*{box-sizing:border-box;margin:0;padding:0}
html,body{width:1200px;height:2517px;overflow:hidden}
body{font-family:"Open Sans",Arial,sans-serif;color:var(--ink);background:var(--white);position:relative}
a{color:inherit;text-decoration:none}
ul{list-style:none}
.wrap{width:880px;margin:0 auto;position:relative}

/* header */
.site-header{height:117px;border-top:5px solid var(--red);background:var(--white)}
.site-header .wrap{height:112px}
.brand{position:absolute;left:0;top:36px;display:flex;align-items:center;gap:10px;font-family:"Cinzel",Georgia,serif;font-weight:500;font-size:21px;color:#555;letter-spacing:.5px}
.brand-mark{width:12px;height:12px;background:var(--red)}
.lang{position:absolute;right:0;top:27px;font-size:10px;font-weight:700;color:var(--red);display:flex;align-items:center;gap:6px}
.lang .dot{width:5px;height:5px;background:var(--red);border-radius:50%}
.main-nav{position:absolute;right:0;top:64px;display:flex;gap:20px;font-size:10px;font-weight:600;color:#555;align-items:center}
.main-nav a{padding-bottom:8px;border-bottom:3px solid transparent}
.main-nav a.active{color:var(--red);border-color:var(--red)}
.main-nav svg{margin-bottom:10px}

/* hero */
.hero{height:563px;position:relative;background:linear-gradient(180deg,#7fa6cf 0%,#b8cde2 28%,#5a6e5a 48%,#3f5a4a 56%,#6f92ad 66%,#4a6a7f 100%)}
.hero-copy{position:absolute;right:160px;top:175px;text-align:right;color:var(--white)}
.hero-copy .kicker{font-size:13px;font-weight:700;letter-spacing:.5px}
.hero-copy h1{font-size:30px;font-weight:700;letter-spacing:1px;margin-top:18px}
.finder{position:absolute;left:160px;top:386px;width:880px;height:98px;background:rgba(20,20,20,.6);padding:14px 22px}
.finder h2{font-size:11px;font-weight:700;color:var(--white);letter-spacing:.5px}
.finder-row{display:flex;gap:12px;margin-top:22px}
.field{height:30px;width:160px;border:1px solid rgba(255,255,255,.55);color:var(--white);font-size:8px;font-weight:600;display:flex;align-items:center;justify-content:space-between;padding:0 9px}
.btn-search{margin-left:auto;width:120px;height:30px;background:var(--red);color:var(--white);font-size:12px;font-weight:700;display:flex;align-items:center;justify-content:center;letter-spacing:.5px}

/* services */
.services{height:265px;padding-top:90px}
.services .wrap{display:flex;justify-content:space-between}
.service{width:188px;height:84px;background:var(--white);box-shadow:0 1px 6px rgba(0,0,0,.12);padding:20px 12px;position:relative}
.service h3{font-size:10px;font-weight:400;color:#555}
.service p{font-size:9px;font-style:italic;color:var(--red);margin-top:4px}
.service .go{position:absolute;right:-4px;top:33px}
.service .go.round{right:-16px;top:28px;width:30px;height:30px;border-radius:50%;background:var(--red);display:flex;align-items:center;justify-content:center}

/* tours */
.tours{background:var(--panel);height:845px;padding-top:34px}
.section-title{text-align:center;font-size:18px;font-weight:600;color:var(--ink);letter-spacing:.5px}
.section-title::after{content:"";display:block;width:108px;height:3px;background:var(--red);margin:12px auto 0}
.tour-grid{display:grid;grid-template-columns:repeat(4,190px);justify-content:space-between;row-gap:45px;margin-top:56px}
.tour-card{height:187px;background:var(--white);padding:14px 12px;box-shadow:0 1px 3px rgba(0,0,0,.06)}
.tour-photo{height:103px}
.tour-card h3{font-size:10px;font-weight:600;color:#555;margin-top:14px}
.tour-card .more{display:block;text-align:right;font-size:9px;color:var(--red);margin-top:14px}

/* booking */
.booking{height:230px;padding-top:42px}
.booking-box{height:140px;border:1px solid var(--line);display:flex;align-items:center;padding:0 40px}
.booking-box h2{font-size:38px;font-weight:400;color:#555;line-height:1.05}
.booking-box h2 span{display:block;color:var(--red);font-size:24px;margin-left:230px}
.btn-book{margin-left:auto;width:160px;height:45px;background:var(--red);color:var(--white);font-size:16px;font-weight:700;display:flex;align-items:center;justify-content:center}

/* footer */
.site-footer{background:var(--footer);height:447px;color:var(--footer-text);padding-top:58px}
.site-footer .wrap{display:grid;grid-template-columns:292px 302px 1fr}
.site-footer h4{font-size:11px;font-weight:700;color:var(--white);letter-spacing:.4px;margin-bottom:18px}
.nav-cols{display:flex;gap:55px;font-size:9px;line-height:20px}
.fl-block{margin-top:40px}
.link-list{font-size:9px;line-height:20px}
.clients{display:flex;gap:22px;align-items:center;margin-top:8px}
.badge{width:64px;height:64px;border-radius:50%;border:2px solid #9a9a9a}
.client-name{font-size:16px;font-weight:700;color:#d6d6d6}
.cards{display:grid;grid-template-columns:repeat(4,44px);gap:8px}
.card{height:24px;background:#e9e9e9;color:#444;font-size:7px;font-weight:700;display:flex;align-items:center;justify-content:center}
.contact-list{font-size:9px;line-height:16px}
.contact-list li{display:flex;gap:12px;margin-bottom:8px;align-items:flex-start}
.map{width:280px;height:112px;background:linear-gradient(135deg,#e8e5dc,#d8dfd0 55%,#e3ddcf)}
.footer-bottom{position:absolute;left:0;top:2467px;width:1200px;height:50px;background:var(--footer-bottom);color:#999;font-size:9px}
.footer-bottom .wrap{height:50px;display:flex;align-items:center;justify-content:space-between}
.social{display:flex;gap:14px}
.social a{display:flex;align-items:center;gap:5px;color:#ccc}
.social i{width:8px;height:8px;background:#ccc}
</style>
</head>
<body>

<header class="site-header">
  <div class="wrap">
    <a class="brand" href="#"><span class="brand-mark"></span>Velmora Journeys</a>
    <div class="lang"><span class="dot"></span>ENGLISH
      <svg width="14" height="14" viewBox="0 0 14 14"><circle cx="7" cy="7" r="6" fill="none" stroke="#888" stroke-width="1.2"/><path d="M1 7h12M7 1c-3 3-3 9 0 12M7 1c3 3 3 9 0 12" fill="none" stroke="#888" stroke-width="1"/></svg>
    </div>
    <nav class="main-nav">
      <a class="active" href="#">HOME</a><a href="#">FJORDS</a><a href="#">CAPITALS</a><a href="#">CRUISES</a><a href="#">WINTER</a><a href="#">PICTURES</a><a href="#">CONTACT</a>
      <svg width="11" height="11" viewBox="0 0 11 11"><circle cx="4.5" cy="4.5" r="3.5" fill="none" stroke="#666" stroke-width="1.4"/><path d="M7 7l3 3" stroke="#666" stroke-width="1.4"/></svg>
    </nav>
  </div>
</header>

<section class="hero" role="img" aria-label="Photograph of steep green mountains rising above a calm bay with red fishing cabins, reflected in the water">
  <div class="hero-copy">
    <p class="kicker">NORWAY'S MOST DRAMATIC MOUNTAIN SCENERY</p>
    <h1>LOFOTEN ISLAND</h1>
  </div>
  <form class="finder">
    <h2>FIND THE TOUR</h2>
    <div class="finder-row">
      <div class="field">TOUR TYPE <svg width="7" height="5"><path d="M0 0h7L3.5 5z" fill="#fff"/></svg></div>
      <div class="field">TOUR SELECTION <svg width="7" height="5"><path d="M0 0h7L3.5 5z" fill="#fff"/></svg></div>
      <div class="field">TRAVEL PERIOD <svg width="9" height="9"><rect x=".5" y="1.5" width="8" height="7" fill="none" stroke="#fff"/><path d="M.5 3.5h8" stroke="#fff"/></svg></div>
      <div class="field">FREE SEARCH</div>
      <div class="btn-search">SEARCH</div>
    </div>
  </form>
</section>

<section class="services">
  <div class="wrap">
    <div class="service"><h3>CUSTOMER PROTECTION</h3><p>4 TOUR AVAILABLE</p><svg class="go" width="6" height="10"><path d="M1 1l4 4-4 4" fill="none" stroke="#555" stroke-width="1.5"/></svg></div>
    <div class="service"><h3>TRAVEL INSURANCE</h3><p>4 TOUR AVAILABLE</p><span class="go round"><svg width="7" height="10"><path d="M1.5 1l4 4-4 4" fill="none" stroke="#fff" stroke-width="1.6"/></svg></span></div>
    <div class="service"><h3>TRAVEL EXPERIENCE</h3><p>4 TOUR AVAILABLE</p><svg class="go" width="6" height="10"><path d="M1 1l4 4-4 4" fill="none" stroke="#555" stroke-width="1.5"/></svg></div>
    <div class="service"><h3>CUSTOMER SERVICE | FAQ</h3><p>4 TOUR AVAILABLE</p><svg class="go" width="6" height="10"><path d="M1 1l4 4-4 4" fill="none" stroke="#555" stroke-width="1.5"/></svg></div>
  </div>
</section>

<section class="tours">
  <div class="wrap">
    <h2 class="section-title">LATEST TOUR PAKAGES</h2>
    <div class="tour-grid">
      <article class="tour-card"><div class="tour-photo" role="img" aria-label="Photograph of a harbour town lit at dusk" style="background:linear-gradient(160deg,#1d3a6e,#3a5fa8 60%,#c9823a)"></div><h3>SCANDINAVIA SPECIALIST</h3><a class="more" href="#">See Tour Details »</a></article>
      <article class="tour-card"><div class="tour-photo" role="img" aria-label="Photograph of a deep fjord seen from a cliff" style="background:linear-gradient(180deg,#9db9d3,#4f6f6a 55%,#3c5a68)"></div><h3>NORWAY TOURS</h3><a class="more" href="#">See Tour Details »</a></article>
      <article class="tour-card"><div class="tour-photo" role="img" aria-label="Photograph of a traveller jumping against a blue sky" style="background:linear-gradient(180deg,#2c7fd0,#7fbaf0)"></div><h3>SPECIAL OFFERS</h3><a class="more" href="#">See Tour Details »</a></article>
      <article class="tour-card"><div class="tour-photo" role="img" aria-label="Photograph of a hand holding a smartphone" style="background:linear-gradient(135deg,#1f4f8a,#6fa6d8 60%,#c8d9ea)"></div><h3>CONTACT</h3><a class="more" href="#">See Tour Details »</a></article>

      <article class="tour-card"><div class="tour-photo" role="img" aria-label="Photograph of a colourful old town waterfront" style="background:linear-gradient(180deg,#8fb2d6,#b98a5a 55%,#5b5e6a)"></div><h3>SWEDEN TOURS</h3><a class="more" href="#">See Tour Details »</a></article>
      <article class="tour-card"><div class="tour-photo" role="img" aria-label="Photograph of steaming geothermal springs" style="background:linear-gradient(180deg,#cfd4d8,#8d969c 60%,#3b4145)"></div><h3>ICELAND TOURS</h3><a class="more" href="#">See Tour Details »</a></article>
      <article class="tour-card"><div class="tour-photo" role="img" aria-label="Photograph of a waterfall in a green valley" style="background:linear-gradient(180deg,#6f8f5a,#c9d6d2 50%,#4a5f3f)"></div><h3>COMBINATION TOURS</h3><a class="more" href="#">See Tour Details »</a></article>
      <article class="tour-card"><div class="tour-photo" role="img" aria-label="Photograph of a dog sled crossing a snowfield" style="background:linear-gradient(180deg,#9fb5cf,#e8edf2 55%,#cfd8e0)"></div><h3>LAPLAND TOURS</h3><a class="more" href="#">See Tour Details »</a></article>

      <article class="tour-card"><div class="tour-photo" role="img" aria-label="Photograph of snow-covered mountain peaks" style="background:linear-gradient(180deg,#3b6fb5,#dfe8f2 60%,#aebfd2)"></div><h3>WINTER TOURS</h3><a class="more" href="#">See Tour Details »</a></article>
      <article class="tour-card"><div class="tour-photo" role="img" aria-label="Photograph of green northern lights over a red-lit landscape" style="background:linear-gradient(180deg,#0e1f2a,#1f7a4a 45%,#8a2a1a)"></div><h3>NORTHERN LIGHTS</h3><a class="more" href="#">See Tour Details »</a></article>
      <article class="tour-card"><div class="tour-photo" role="img" aria-label="Photograph of a fjord between steep green slopes" style="background:linear-gradient(180deg,#7fa3c8,#2f5a46 50%,#1f4a66)"></div><h3>FJORDS TOURS</h3><a class="more" href="#">See Tour Details »</a></article>
      <article class="tour-card"><div class="tour-photo" role="img" aria-label="Photograph of a capital city harbour skyline" style="background:linear-gradient(180deg,#5a9ad6,#d9e3ea 45%,#2a6fa8)"></div><h3>CAPITALS TOUR</h3><a class="more" href="#">See Tour Details »</a></article>
    </div>
  </div>
</section>

<section class="booking">
  <div class="wrap">
    <div class="booking-box">
      <h2>YOUR WINDOW TO BOOKING<span>“THE BEST OF OUR WORLD”</span></h2>
      <a class="btn-book" href="#">BOOK NOW</a>
    </div>
  </div>
</section>

<footer class="site-footer">
  <div class="wrap">
    <div>
      <h4>NAVIGATE</h4>
      <div class="nav-cols">
        <ul><li>HOME</li><li>FJORDS</li><li>CAPITALS</li><li>CRUISES</li></ul>
        <ul><li>WINTER</li><li>PICTURES</li><li>CONTACT</li></ul>
      </div>
      <div class="fl-block">
        <h4>VELMORA JOURNEYS</h4>
        <ul class="link-list">
          <li>ABOUT VELMORA JOURNEYS</li><li>BOOKING AND PAYMENT PROCEDURE</li><li>TERMS AND CONDITIONS</li><li>FREQUENTLY ASKED QUESTIONS (FAQ)</li><li>TRAVEL EXPERIENCES</li><li>PHOTO CREDITS</li><li>SITE MAP</li>
        </ul>
      </div>
    </div>
    <div>
      <h4>OUR CLIENTS</h4>
      <div class="clients"><span class="badge"></span><span class="client-name">Torvind Cars</span></div>
      <div class="fl-block">
        <h4>SUPPORTED CREDIT CARDS</h4>
        <div class="cards">
          <span class="card">Secure</span><span class="card">Nordex</span><span class="card">Kortia</span><span class="card">Runacard</span>
          <span class="card">Elka</span><span class="card">Paylo</span><span class="card">Vantra</span><span class="card">Kortia</span>
        </div>
      </div>
    </div>
    <div>
      <h4>CONTACT US</h4>
      <ul class="contact-list">
        <li><svg width="9" height="12" viewBox="0 0 9 12"><path d="M4.5 0C2 0 0 2 0 4.5 0 8 4.5 12 4.5 12S9 8 9 4.5C9 2 7 0 4.5 0z" fill="#ccc"/><circle cx="4.5" cy="4.5" r="1.7" fill="#2a2a2a"/></svg><span>STORGATA 14, N-0155 OSLO,<br>NORWAY</span></li>
        <li><svg width="10" height="10" viewBox="0 0 10 10"><path d="M2 0l2 2.5-1.2 1.3c.7 1.4 1.8 2.5 3.2 3.2L7.3 5.8 10 8 8.5 10C4 9.5.5 6 0 1.5z" fill="#ccc"/></svg><span>+47 22 41 18 70</span></li>
        <li><svg width="11" height="8" viewBox="0 0 11 8"><rect width="11" height="8" fill="#ccc"/><path d="M0 0l5.5 4.5L11 0" fill="none" stroke="#2a2a2a"/></svg><span>INFO@VELMORA-JOURNEYS.COM</span></li>
      </ul>
      <div class="fl-block" style="margin-top:46px">
        <h4>SITE MAP</h4>
        <div class="map" role="img" aria-label="Street map showing the office location in Oslo"></div>
      </div>
    </div>
  </div>
</footer>
<div class="footer-bottom">
  <div class="wrap">
    <span>Copyright © 2015 · Velmora Journeys AS · All rights reserved.</span>
    <div class="social"><a href="#"><i></i>Fjordbook</a><a href="#"><i></i>Chirpa</a><a href="#"><i></i>Pinvault</a><a href="#"><i></i>Circlet</a></div>
  </div>
</div>

</body>
</html>
```